Ayurveda & Wellness Website Redesign.

I need my website www.palvoreta.com re-skinned. It is a wordpress site with Velo Framer.
I need a clearer funnel for new clients on the home page.
The funnel should provide questions for the potential client to answer. I can provide these, but I need a better funnel mechanism I think,
Possibly a video on the home page. Or an area of a video that I can change out.
So a better landing page is KEY!
The funnel should reroute to a video page and I should get informed when new clients enroll in the funnel.
Maybe I need a management system for this, but I need a recommendation.
Now I am using forms manager.
I need to be able to make changes using wordpress and/or Velo Framer.
The website should have a clean and spiritual feeling.
I can provide many more pictures and higher resolution.
I like the feeling of this website: http://brightfernherbals.com
Also this website: http://lotuscalmhaven.com/sessionswithkoriel/
Target Market(s)
Women ages 25-65. People interested in health, yoga, spirituality.
Industry/Entity Type
Health And Wellness
Coding
Coded - Design and coding required
Requirements
Must have
- A clear sales funnel/enrollment mechanism on the home page. Could have a ebook download (I will provide) when they enroll.
Nice to have
- Currently using Slotra for clients to enroll in appointments. I would like to keep this.

```html
<!DOCTYPE html>
<html lang="en">
<head>
<meta charset="utf-8">
<title>Seek Calm – Ayurveda</title>
<link href="https://fonts.googleapis.com/css2?family=Lato:ital,wght@0,400;0,700;1,400&family=Open+Sans:wght@400;600&display=swap" rel="stylesheet">
<style>
  :root {
    --topbar-green: #5a7008;
    --nav-bg: #e9eff1;
    --nav-text: #1b1b1b;
    --nav-active: #2a55a0;
    --hero-deep: #034866;
    --hero-mid: #0a7496;
    --hero-light: #3fb6d3;
    --white: #ffffff;
    --glass: rgba(255,255,255,0.12);
    --glass-line: rgba(255,255,255,0.55);
    --navy: #15236b;
  }
  * { margin: 0; padding: 0; box-sizing: border-box; }
  html, body { width: 1200px; height: 790px; overflow: hidden; background: var(--white); }
  body { font-family: "Lato", sans-serif; position: relative; }

  .top-bar {
    height: 27px; background: var(--topbar-green); color: var(--white);
    font-family: "Open Sans", sans-serif; font-size: 11px;
    display: flex; align-items: center; gap: 16px; padding-left: 68px;
  }
  .top-bar .contact-item { display: flex; align-items: center; gap: 4px; }
  .top-bar svg { width: 10px; height: 10px; fill: var(--white); }

  .site-nav {
    height: 80px; background: var(--nav-bg);
    display: flex; align-items: center; padding: 0 68px 0 71px;
  }
  .brand { font-size: 31px; font-weight: 400; color: var(--nav-text); }
  .menu { margin-left: auto; display: flex; gap: 28px; list-style: none; align-items: center; }
  .menu a {
    text-decoration: none; color: var(--nav-text); font-size: 12.5px; font-weight: 700;
    letter-spacing: 1px; text-transform: uppercase;
  }
  .menu a.active { color: var(--nav-active); font-weight: 400; }
  .search-icon { width: 15px; height: 15px; margin-left: 4px; margin-top: -8px; }

  .hero { position: relative; height: 556px; overflow: hidden; }
  .hero-backdrop {
    position: absolute; inset: 0;
    background: linear-gradient(100deg, var(--hero-deep) 0%, var(--hero-mid) 45%, var(--hero-light) 80%, #7fd0e2 100%);
  }

  .video-area {
    position: absolute; left: 720px; top: 20px; width: 420px; height: 516px;
    background:
      radial-gradient(ellipse 170px 120px at 145px 420px, rgba(255,255,255,0.95), rgba(255,255,255,0.3) 55%, rgba(255,255,255,0) 100%),
      radial-gradient(ellipse 220px 250px at 180px 200px, rgba(200,240,255,0.45), rgba(200,240,255,0) 100%);
  }
  .video-play {
    position: absolute; left: 150px; top: 230px; width: 64px; height: 64px;
  }
  .video-caption {
    position: absolute; left: 0; width: 364px; top: 304px; text-align: center;
    font-family: "Open Sans", sans-serif; font-size: 14px; color: var(--white);
    text-shadow: 0 1px 2px rgba(0,0,0,0.35);
  }

  .hero-content { position: absolute; left: 186px; top: 202px; color: var(--white); width: 520px; }
  .hero-title {
    font-size: 33px; font-weight: 700; letter-spacing: 0.8px; text-transform: uppercase;
    text-shadow: 0 1px 3px rgba(0,0,0,0.3); white-space: nowrap;
  }
  .hero-subtitle {
    font-family: "Open Sans", sans-serif; font-size: 23px; font-weight: 400;
    margin-top: 35px; text-shadow: 0 1px 2px rgba(0,0,0,0.25);
  }

  .funnel {
    margin-top: 28px; padding: 16px 18px 18px; width: 470px;
    background: var(--glass); border: 1px solid var(--glass-line); border-radius: 4px;
  }
  .funnel-step {
    font-family: "Open Sans", sans-serif; font-size: 11px; letter-spacing: 1.2px;
    text-transform: uppercase; opacity: 0.85;
  }
  .funnel-question { font-size: 18px; font-weight: 700; margin-top: 6px; }
  .funnel-options { display: flex; gap: 10px; margin-top: 12px; }
  .funnel-option {
    font-family: "Open Sans", sans-serif; font-size: 13px; color: var(--white);
    padding: 6px 12px; border: 1px solid var(--glass-line); border-radius: 16px;
  }
  .funnel-option.selected { background: var(--white); color: var(--hero-deep); border-color: var(--white); }
  .funnel-action { display: flex; align-items: center; gap: 16px; margin-top: 16px; }
  .hero-button {
    display: inline-block; padding: 7px 18px;
    border: 2px solid var(--white); border-radius: 3px;
    font-family: "Open Sans", sans-serif; font-size: 18px; color: var(--white); text-decoration: none;
  }
  .funnel-note { font-family: "Open Sans", sans-serif; font-size: 12.5px; line-height: 1.4; opacity: 0.9; }

  .intro-heading {
    position: absolute; top: 745px; left: 0; width: 100%; text-align: center;
    font-size: 29px; font-weight: 400; color: var(--navy);
  }
  .intro-heading em { font-style: italic; }
</style>
</head>
<body>
  <div class="top-bar">
    <span class="contact-item">
      <svg viewBox="0 0 10 10"><path d="M2 0.5l1.8 2-1 1.2a6 6 0 0 0 3.5 3.5l1.2-1 2 1.8-1 1.8C4 9.5 0.5 6 0.2 1.5z"/></svg>
      707-555-0142
    </span>
    <span class="contact-item">
      <svg viewBox="0 0 12 10"><path d="M0 1h12v1L6 5.5 0 2z M0 3.2l6 3.5 6-3.5V9H0z"/></svg>
      marisolvane@mailbox.com
    </span>
  </div>

  <header class="site-nav">
    <div class="brand">Seek Calm</div>
    <ul class="menu">
      <li><a class="active" href="#">Home</a></li>
      <li><a href="#">Consults</a></li>
      <li><a href="#">Ayurveda</a></li>
      <li><a href="#">About Marisol</a></li>
      <li><a href="#">Workshops</a></li>
      <li><a href="#">Follow the Blog</a></li>
      <li><a href="#">Contact Us</a></li>
      <li>
        <svg class="search-icon" viewBox="0 0 16 16" fill="none" stroke="#1b1b1b" stroke-width="1.4">
          <circle cx="9.5" cy="6.5" r="5"/><line x1="6" y1="10" x2="1.5" y2="14.5"/>
        </svg>
      </li>
    </ul>
  </header>

  <section class="hero">
    <div class="hero-backdrop"></div>

    <div class="video-area" role="img" aria-label="Swappable welcome video: glowing white lotus on calm turquoise water with sparkling light">
      <svg class="video-play" viewBox="0 0 64 64">
        <circle cx="32" cy="32" r="30" fill="rgba(255,255,255,0.2)" stroke="#ffffff" stroke-width="2"/>
        <path d="M26 20 L46 32 L26 44 Z" fill="#ffffff"/>
      </svg>
      <p class="video-caption">Watch: a welcome from Marisol</p>
    </div>

    <div class="hero-content">
      <h1 class="hero-title">Seek Calm with Ayurveda</h1>
      <p class="hero-subtitle">Let our Treatment’s warmth work for you!</p>

      <form class="funnel">
        <p class="funnel-step">Step 1 of 3 · Find your path</p>
        <p class="funnel-question">What would you like to balance first?</p>
        <div class="funnel-options">
          <span class="funnel-option selected">Sleep &amp; Stress</span>
          <span class="funnel-option">Digestion</span>
          <span class="funnel-option">Energy</span>
          <span class="funnel-option">Skin</span>
        </div>
        <div class="funnel-action">
          <a class="hero-button" href="#">Get Started Today !</a>
          <p class="funnel-note">3 short questions, then your<br>free e-book and video.</p>
        </div>
      </form>
    </div>
  </section>

  <h2 class="intro-heading">Ayurvedic Wellness <em>a year – long course to establish.</em></h2>
</body>
</html>
```